Summit Basin Operators, Inc. Company Brochure

I would like someone to design a brochure that can be handed out to prospective clients. We are a full service water and wastewater operations company that provides services to Municipal Utility Districts and citys. I would like something that is catchy to the eye and reflects a company that prides itself on providing personal service to its clients. We need to revamp our website, that's next, but the website does have a description of our company and services offered. You can find that information at www.summitbasinoperators.example

```html
<!DOCTYPE html>
<html lang="en">
<head>
<meta charset="utf-8">
<title>Summit Basin Operators, Inc. – Brochure</title>
<link rel="stylesheet" href="https://fonts.googleapis.com/css2?family=Source+Sans+3:wght@400;600;700&display=swap">
<style>
:root{
  --brand:#1a7fd4;
  --brand-dark:#0d5fae;
  --ink:#2b3440;
  --band-light:#d6ebfb;
  --band-mid:#9fd0f5;
  --water-deep:#0b4fa8;
  --water-bright:#2f8fe0;
  --page:#ffffff;
  --backdrop:#e9ecef;
}
*{box-sizing:border-box;margin:0;padding:0}
html,body{width:1185px;height:1200px;overflow:hidden;background:var(--backdrop);font-family:"Source Sans 3",sans-serif;color:var(--ink)}
.spread{position:absolute;left:32px;width:1120px;height:560px;background:var(--page);box-shadow:0 2px 10px rgba(0,0,0,.18);overflow:hidden}
.spread--outside{top:24px}
.spread--inside{top:616px}
.spread__fold{position:absolute;left:560px;top:0;width:1px;height:100%;background:rgba(0,0,0,.08);z-index:5}
.spread__art{position:absolute;inset:0;width:1120px;height:560px}
.page{position:absolute;top:0;width:560px;height:560px}
.page--left{left:0}.page--right{left:560px}
.section-title{display:flex;align-items:center;gap:10px;color:var(--brand);font-weight:600;font-size:27px;line-height:1}
.section-title__dot{width:18px;height:18px;border:3px solid var(--brand);border-radius:50%}
.body-copy{font-size:10.5px;line-height:1.3;text-align:justify}
.mission{position:absolute;left:22px;top:20px;width:318px}
.mission .body-copy{margin-top:16px}
.mission .body-copy+.body-copy{margin-top:12px}
.cover-id{position:absolute;left:0;top:30px;width:560px;text-align:center}
.cover-id__dot{display:inline-block;width:28px;height:28px;border:4px solid var(--brand);border-radius:50%}
.cover-id__name{color:var(--brand);font-weight:600;font-size:24px;margin-top:8px}
.cover-id__tag{color:var(--brand-dark);font-size:15px;margin-top:4px}
.contact{position:absolute;left:26px;top:452px;font-size:14px;color:var(--ink);line-height:1.2}
.contact strong{color:var(--brand-dark);font-weight:700}
.contact__addr{font-size:13px;margin-top:4px}
.web{position:absolute;right:50px;bottom:18px;font-size:12px;font-weight:700;color:var(--ink)}
.about{position:absolute;left:32px;top:18px;width:310px}
.about .body-copy{margin-top:14px;font-size:11px;line-height:1.2}
.bios{position:absolute;left:20px;top:260px;width:330px}
.bio{display:flex;align-items:flex-start;gap:14px;margin-bottom:12px}
.bio__photo{flex:none;width:64px;height:64px;border-radius:50%;background:radial-gradient(circle at 50% 40%,#c9a58a,#6f5a4c);border:3px solid #fff;box-shadow:0 1px 3px rgba(0,0,0,.2)}
.bio__text{font-size:9px;line-height:1.2;text-align:justify;background:rgba(255,255,255,.75);border-radius:8px;padding:5px 8px}
.bio__text strong{font-size:10px}
.services{position:absolute;left:26px;top:18px;width:310px}
.services .body-copy{margin-top:12px;font-size:11px;line-height:1.15}
.services__lead{font-size:11px;font-weight:700;margin-top:6px}
.service-list{list-style:none;margin-top:8px}
.service-list li{position:relative;padding-left:16px;font-size:11.5px;font-weight:700;line-height:1.15;margin-bottom:3px}
.service-list li::before{content:"";position:absolute;left:0;top:4px;width:7px;height:7px;border-radius:50%;background:var(--brand)}
.ops-banner{position:absolute;left:0;bottom:0;width:560px;height:118px;background:linear-gradient(180deg,#7fc0f0 0%,var(--water-bright) 45%,var(--water-deep) 100%)}
.ops-banner__photo{position:absolute;left:40px;top:10px;width:70px;height:100px;border-radius:6px;background:linear-gradient(180deg,rgba(255,255,255,.55),rgba(255,255,255,.15))}
.ops-banner__text{position:absolute;right:22px;bottom:16px;color:#fff;font-weight:700;font-size:19px;text-align:right;line-height:1.1}
</style>
</head>
<body>

<section class="spread spread--outside">
  <svg class="spread__art" viewBox="0 0 1120 560">
    <defs>
      <linearGradient id="water-outside" x1="0" y1="0" x2="0" y2="1">
        <stop offset="0" stop-color="#1f6fcc"/><stop offset=".5" stop-color="#3a96e4"/><stop offset="1" stop-color="#0d4fa6"/>
      </linearGradient>
    </defs>
    <path d="M0 190 C300 150 700 220 1120 150 L1120 470 C700 520 300 470 0 520 Z" fill="var(--band-light)"/>
    <path d="M0 200 C300 162 700 228 1120 160" fill="none" stroke="var(--brand)" stroke-width="4"/>
    <g role="img" aria-label="Close-up photograph of blue water droplets">
      <path d="M0 268 C300 230 700 290 1120 232 L1120 395 C700 450 300 400 0 430 Z" fill="url(#water-outside)"/>
    </g>
    <path d="M0 440 C300 410 700 450 1120 420 L1120 520 C700 560 300 520 0 560 Z" fill="var(--band-mid)" opacity=".45"/>
    <path d="M0 552 C400 520 800 540 1120 505" fill="none" stroke="var(--brand)" stroke-width="3"/>
  </svg>
  <div class="spread__fold"></div>

  <div class="page page--left">
    <div class="mission">
      <h2 class="section-title"><span class="section-title__dot"></span>Our Mission</h2>
      <p class="body-copy">Summit Basin Operators, Inc. is a leading competitor in the utility operations industry and has achieved this status by maintaining the quality of work and relationships that few companies can offer.</p>
      <p class="body-copy">Whether you are a District that is currently operated by an outside contract company or a District entertaining the concept, Summit Basin Operators, Inc would be delighted to present a detailed quote for operations and services. Please contact our office and a representative will discuss the services that are currently available in your area.</p>
    </div>
    <div class="contact">
      <div>Office: <strong>281-555-0142</strong></div>
      <div>Toll Free <strong>877-555-0199</strong></div>
      <div class="contact__addr">4820 Ridgecrest Rd #210<br>Crosby, TX 77532</div>
    </div>
  </div>

  <div class="page page--right">
    <div class="cover-id">
      <span class="cover-id__dot"></span>
      <h1 class="cover-id__name">Summit Basin Operators Inc.</h1>
      <p class="cover-id__tag">A Full Service Operations Company</p>
    </div>
    <p class="web">www.summitbasinoperators.example</p>
  </div>
</section>

<section class="spread spread--inside">
  <svg class="spread__art" viewBox="0 0 1120 560">
    <path d="M0 225 C200 205 400 240 560 225 L560 560 L0 560 Z" fill="var(--band-light)"/>
    <path d="M0 232 C200 212 400 248 560 232" fill="none" stroke="var(--brand)" stroke-width="3"/>
    <path d="M0 300 C200 270 400 320 560 290 L560 470 C400 500 200 460 0 500 Z" fill="var(--band-mid)" opacity=".4"/>
  </svg>
  <div class="spread__fold"></div>

  <div class="page page--left">
    <div class="about">
      <h2 class="section-title"><span class="section-title__dot"></span>About Us</h2>
      <p class="body-copy">Summit Basin Operators, Inc. was incorporated in the state of Texas in 1989. Summit Basin Operators, Inc. is a water and waste water utility operations and billing company. All personnel employed by Summit Basin Operators, Inc. are licensed by the TCEQ in water &amp; waste water operations and obtain the proper training needed to successfully operate treatment plants to their maximum capability. We are certified to operate surface water, ground water, and waste water treatment facilities to their maximum capability. We have a fully staffed billing and collections office to handle any of your customers needs. The mission of Summit Basin Operators, Inc. is to provide the consumer with the highest caliber of services available. Our goal is to achieve this service for the Districts with the most competitive cost around.</p>
    </div>
    <div class="bios">
      <div class="bio">
        <div class="bio__photo" role="img" aria-label="Portrait photo of the company president"></div>
        <p class="bio__text"><strong>Marian Kessler</strong> is the President and CEO of Summit Basin Operators and has 30 years of experience in the Water and Waste Water, Billing and Collections Industry. Mrs. Kessler serves as the Districts liaison.</p>
      </div>
      <div class="bio">
        <div class="bio__photo" role="img" aria-label="Portrait photo of the office manager"></div>
        <p class="bio__text"><strong>Laura Benning</strong> is the Office Manager and has been with Summit Basin Operators since 1994. Laura has 20 years experience in the industry and handles over 3000 accounts as well as oversees the day to day customer care. She believes that customer care is one of the most important aspects of her job. She makes it a point to get to know your residents so we can better service their needs. If you have any questions please feel free to contact her at 281-555-0142</p>
      </div>
      <div class="bio">
        <div class="bio__photo" role="img" aria-label="Portrait photo of the district manager"></div>
        <p class="bio__text"><strong>Tyler Haskins</strong> serves as District Manager and has been employed with Summit Basin Operators, Inc. since 2002. He has over 16 years of experience in the municipal utility industry and currently holds a Class A Water, Class A Wastewater, and Customer Service Inspection license issued by the TCEQ.</p>
      </div>
    </div>
  </div>

  <div class="page page--right">
    <div class="services">
      <h2 class="section-title"><span class="section-title__dot"></span>Services</h2>
      <p class="body-copy">Summit Basin Operators, Inc. is a “full service” operations company that handles all aspects of operations in the water/waste water utility industry.</p>
      <p class="body-copy">Here at Summit Basin Operators, Inc., we feel that it is important to provide the highest caliber of services available to the Districts in which we operate. We offer the ability to tailor our services based on the current needs of the District</p>
      <p class="services__lead">Services currently available are:</p>
      <ul class="service-list">
        <li>Surface Water Plant Operations</li>
        <li>Waste Water Plant Operations</li>
        <li>Ground Water Well Operations</li>
        <li>Distribution and Collection System maintenance and repairs</li>
        <li>New Construction Water and Sewer Taps, and all inspections required</li>
        <li>Billing and Collections</li>
        <li>Meter Reading</li>
        <li>Consulting/Management</li>
        <li>Lab Work and Reporting to any and all regulating agencies</li>
        <li>Project Planning</li>
        <li>Assist in Annual Budget Planning</li>
        <li>Smoke Testing</li>
        <li>Park and Trail maintenance</li>
        <li>Detention pond maintenance</li>
      </ul>
    </div>
    <div class="ops-banner" role="img" aria-label="Photograph of water pouring into a glass against a blue background">
      <div class="ops-banner__photo"></div>
      <p class="ops-banner__text">We are a 24/7<br>Operations Company!</p>
    </div>
  </div>
</section>

</body>
</html>
```